Corvale Motorized Shade Business Card

Hello, we've had our logo made. Now we are looking for a clean and cool looking business card. One side can just be the logo with any design elements that might look good with it. The other side will be Name, Phone Number and Email. There will not be an address on the card.

```html
<!DOCTYPE html>
<html lang="en">
<head>
<meta charset="utf-8">
<title>Corvale Motorized Shade – Business Card</title>
<link rel="stylesheet" href="https://fonts.googleapis.com/css2?family=Oswald:wght@500;600&family=Open+Sans:wght@400&display=swap">
<style>
  :root {
    --navy: #0b3770;
    --sky: #009fdf;
    --sun: #f0b616;
    --paper: #f3f3f3;
    --stage: #3b3b3b;
  }
  * { box-sizing: border-box; margin: 0; padding: 0; }
  html, body { width: 1200px; height: 1021px; overflow: hidden; }
  body {
    background: var(--stage);
    position: relative;
    font-family: "Open Sans", sans-serif;
  }
  .card {
    position: absolute;
    left: 240px;
    width: 720px;
    height: 411px;
    overflow: hidden;
  }
  .card--back { top: 60px; background: var(--navy); }
  .card--front { top: 550px; background: var(--paper); }

  .brand {
    font-family: "Oswald", sans-serif;
    font-weight: 600;
    text-transform: uppercase;
    display: flex;
    align-items: center;
    gap: 14px;
    line-height: 1;
  }
  .brand__dot { width: 18px; height: 18px; border-radius: 50%; background: currentColor; flex: none; }
  .card--back .brand {
    position: absolute; left: 0; right: 0; top: 0; bottom: 0;
    justify-content: center;
    color: #ffffff;
    font-size: 46px;
    letter-spacing: 2px;
  }
  .card--front .brand {
    position: absolute; left: 46px; top: 52px;
    color: var(--navy);
    font-size: 34px;
    letter-spacing: 1px;
  }
  .card--front .brand .brand__dot { width: 14px; height: 14px; }

  .contact {
    position: absolute; left: 46px; top: 222px;
    list-style: none;
    color: var(--navy);
    font-size: 19px;
    line-height: 28px;
  }
  .contact li { display: flex; align-items: center; gap: 8px; }
  .contact svg { width: 16px; height: 16px; flex: none; }

  .person {
    position: absolute; right: 60px; top: 150px;
    text-align: right;
  }
  .person__name {
    font-family: "Oswald", sans-serif;
    font-weight: 600;
    font-size: 30px;
    color: var(--navy);
    text-transform: uppercase;
    letter-spacing: 0.5px;
    line-height: 1.1;
  }
  .person__role {
    font-family: "Open Sans", sans-serif;
    font-size: 19px;
    color: var(--sky);
    text-transform: uppercase;
    letter-spacing: 1px;
  }

  .footer-band {
    position: absolute; left: 0; right: 0; bottom: 0; height: 16px;
    background: var(--navy);
  }
  .footer-band__accent { position: absolute; top: 0; height: 100%; width: 64px; }
  .footer-band__accent--sky { right: 130px; background: var(--sky); border-left: 3px solid #fff; }
  .footer-band__accent--sun { right: 63px; background: var(--sun); border-left: 3px solid #fff; border-right: 3px solid #fff; }
</style>
</head>
<body>
  <section class="card card--back" aria-label="Card back">
    <div class="brand"><span class="brand__dot"></span>Corvale Motorized Shades</div>
  </section>

  <section class="card card--front" aria-label="Card front">
    <div class="brand"><span class="brand__dot"></span>Corvale Motorized Shades</div>

    <ul class="contact">
      <li>
        <svg viewBox="0 0 16 16" aria-hidden="true"><path fill="var(--sun)" d="M3.5 1.5l2.6 2.6-1.5 2a9 9 0 0 0 5.3 5.3l2-1.5 2.6 2.6-1.7 2C7 14 2 9 1.5 3.2z"/></svg>
        (555) 014-2276
      </li>
      <li>
        <svg viewBox="0 0 16 16" aria-hidden="true"><rect x="1" y="3" width="14" height="10" fill="none" stroke="var(--sun)" stroke-width="1.6"/><path d="M1 3l7 6 7-6" fill="none" stroke="var(--sun)" stroke-width="1.6"/></svg>
        daniel@corvalemotorizedshades.com
      </li>
      <li>
        <svg viewBox="0 0 16 16" aria-hidden="true"><circle cx="8" cy="8" r="6.5" fill="none" stroke="var(--sun)" stroke-width="1.5"/><ellipse cx="8" cy="8" rx="3" ry="6.5" fill="none" stroke="var(--sun)" stroke-width="1.2"/><path d="M1.5 8h13" stroke="var(--sun)" stroke-width="1.2"/></svg>
        www.corvalemotorizedshades.com
      </li>
    </ul>

    <div class="person">
      <p class="person__name">Daniel Hartwell</p>
      <p class="person__role">Owner</p>
    </div>

    <div class="footer-band">
      <span class="footer-band__accent footer-band__accent--sky"></span>
      <span class="footer-band__accent footer-band__accent--sun"></span>
    </div>
  </section>
</body>
</html>
```